Lawyers in the Netherlands website + logo

We are going in 2015 to launch a website where all law firms in the Netherlands and have the opportunity to place an ad program.

The domain name wil be:

kwelderhofpunt.website

We want a responsive PSD bootstrap twitter 1170 pixel grid.
for the homepage, result page and the detail page of the customer.

This sites we like:
https://www.vorqami.com/lawyers

https://lawyers.vorqami.com/lawyer/tad-mirske-5820734

http://solicitordirectory.brevmoor.co.uk/
Map of the Netherlands?

http://solicitordirectory.brevmoor.co.uk/listing/category-search/commercial
http://www.quellbarn.com.au/find-a-lawyer/banking-finance-law/

```html
<!DOCTYPE html>
<html lang="en">
<head>
<meta charset="utf-8">
<title>Kwelderhofpunt – We Provide Legal Help</title>
<link rel="stylesheet" href="https://fonts.googleapis.com/css2?family=Montserrat:wght@400;700&family=Noto+Serif:wght@400&family=Open+Sans:wght@400;600;700&display=swap">
<style>
:root{
  --navy:#0c1e5b;
  --ink:#333a45;
  --muted:#5a5f68;
  --white:#ffffff;
  --line:#e2e4e8;
  --footer:#1d1d1f;
}
*{margin:0;padding:0;box-sizing:border-box}
html,body{width:1200px;height:2826px;overflow:hidden;background:var(--white)}
body{font-family:"Open Sans",Arial,sans-serif;color:var(--ink);position:relative}
.heading{font-family:"Montserrat",Arial,sans-serif;font-weight:700;text-transform:uppercase}
.serif{font-family:"Noto Serif",Georgia,serif}

/* hero */
.hero{position:absolute;left:0;top:0;width:1200px;height:622px;
  background:linear-gradient(180deg,#14295e 0%,#1f3f7a 45%,#2b3a5a 70%,#121a2c 100%);color:var(--white)}
.hero-photo{position:absolute;inset:0}
.brand{position:absolute;left:62px;top:50px;font-family:"Montserrat",Arial,sans-serif;font-weight:700;font-size:31px;letter-spacing:.5px;color:var(--white)}
.main-nav{position:absolute;right:60px;top:66px;display:flex;gap:34px}
.main-nav a{font-family:"Montserrat",Arial,sans-serif;font-size:15px;color:var(--white);text-decoration:none;text-transform:uppercase}
.hero h1{position:absolute;left:0;width:1200px;top:272px;text-align:center;font-size:62px;line-height:72px;letter-spacing:.5px}
.hero .tagline{position:absolute;left:0;width:1200px;top:357px;text-align:center;font-size:22px;line-height:30px}
.btn-outline{position:absolute;display:flex;align-items:center;justify-content:center;border:2px solid var(--white);color:var(--white);text-decoration:none;font-family:"Montserrat",Arial,sans-serif;font-weight:700;font-size:16px;text-transform:uppercase;border-radius:3px}
.hero .btn-outline{left:478px;top:420px;width:245px;height:53px}
.dots{position:absolute;left:0;width:1200px;display:flex;justify-content:center;gap:15px}
.dots span{width:11px;height:11px;border-radius:50%;background:rgba(255,255,255,.45)}
.dots span.on{background:var(--white)}
.hero .dots{top:588px}

/* section headings */
.section-title{position:absolute;left:0;width:1200px;text-align:center;font-size:28px;line-height:34px;color:var(--navy)}
.section-lead{position:absolute;left:50px;width:1100px;text-align:center;font-size:16px;line-height:22px;color:var(--muted)}

/* practice areas */
.practice .section-title{top:666px}
.practice .section-lead{top:718px}
.area-grid{position:absolute;left:60px;top:818px;display:flex;gap:16px}
.area{width:258px;height:214px;background:var(--navy);display:flex;flex-direction:column;align-items:center;color:var(--white)}
.area svg{margin-top:50px;width:76px;height:76px}
.area h3{margin-top:26px;font-size:16px}

/* about */
.about{position:absolute;left:0;top:1106px;width:1200px;height:320px;
  background:linear-gradient(90deg,#2a2d31 0%,#4a4f55 40%,#3a3e44 70%,#24272b 100%);color:var(--white)}
.about h2{position:absolute;left:0;width:1200px;top:42px;text-align:center;font-size:27px}
.about .quote{position:absolute;left:0;width:1200px;top:100px;text-align:center;font-size:17px}
.about .summary{position:absolute;left:62px;width:1076px;top:148px;text-align:center;font-size:13px;line-height:22px;color:#d8dbe0}
.about .btn-outline{left:535px;top:230px;width:130px;height:49px;font-size:16px}

/* lawyers */
.lawyers .section-title{top:1487px}
.lawyers .section-lead{top:1540px}
.lawyer-grid{position:absolute;left:60px;top:1616px;display:flex;gap:16px}
.lawyer{width:258px;height:438px;border:1px solid var(--line);text-align:center;position:relative}
.lawyer .photo{height:189px;background:linear-gradient(135deg,#8a96a8,#c9ced6 60%,#e6e8ec)}
.lawyer h3{margin-top:18px;font-size:21px;line-height:28px;font-weight:400;color:var(--navy)}
.lawyer .role{margin-top:2px;font-size:16px;color:var(--ink)}
.lawyer p{margin:12px 8px 0;font-size:12px;line-height:22px;color:var(--ink)}
.btn-solid{position:absolute;left:75px;top:367px;width:106px;height:49px;background:var(--navy);color:var(--white);border-radius:3px;display:flex;align-items:center;justify-content:center;text-decoration:none;font-weight:700;font-size:15px}

/* testimonials */
.testimonials{position:absolute;left:0;top:2104px;width:1200px;height:321px;background:var(--navy);color:var(--white)}
.testimonials h2{position:absolute;left:0;width:1200px;top:42px;text-align:center;font-size:29px}
.avatar{position:absolute;left:62px;top:104px;width:123px;height:123px;border-radius:50%;border:4px solid var(--white);background:linear-gradient(160deg,#8a5a48,#d8b29c)}
.testimonials blockquote{position:absolute;left:228px;top:118px;width:912px;font-size:13px;line-height:22px;color:#e4e7ef}
.testimonials cite{position:absolute;left:228px;top:218px;font-style:normal;font-weight:700;font-size:15px}
.testimonials .dots{top:270px}
.testimonials .dots span{width:15px;height:15px;background:transparent;border:2px solid var(--white)}
.testimonials .dots span.on{background:var(--white)}

/* map */
.map{position:absolute;left:0;top:2425px;width:1200px;height:282px;background:linear-gradient(180deg,#626467,#55575a)}

/* footer */
.site-footer{position:absolute;left:0;top:2707px;width:1200px;height:119px;background:var(--footer);color:var(--white)}
.footer-nav{position:absolute;left:60px;top:40px;display:flex;gap:28px}
.footer-nav a{font-size:13px;color:var(--white);text-decoration:none;text-transform:uppercase}
.copyright{position:absolute;left:60px;top:68px;font-size:13px}
.social{position:absolute;left:1038px;top:52px;display:flex;gap:14px}
.social span{width:24px;height:24px;border-radius:4px;background:var(--white)}
</style>
</head>
<body>

<header class="hero">
  <div class="hero-photo" role="img" aria-label="Night skyline of a harbour city with a cable bridge over the river"></div>
  <div class="brand">KWELDERHOFPUNT</div>
  <nav class="main-nav">
    <a href="#">Home</a><a href="#">Practice Areas</a><a href="#">Lawyers</a><a href="#">News</a><a href="#">FAQ</a><a href="#">Contact</a>
  </nav>
  <h1 class="heading">We Provide Legal Help</h1>
  <p class="tagline serif">We are a full service, general practice law firm</p>
  <a class="btn-outline" href="#">Free Case Evaluation</a>
  <div class="dots"><span></span><span class="on"></span><span></span></div>
</header>

<section class="practice">
  <h2 class="section-title heading">Practice Areas</h2>
  <p class="section-lead serif">We are a full service, general practice law firm, but we specialize in the areas of residential and commercial real estate transactions and litigation<br>and commercial transactions and litigation</p>
  <div class="area-grid">
    <div class="area">
      <svg viewBox="0 0 76 76" fill="#fff"><path d="M38 6 6 22v6h64v-6z"/><rect x="12" y="32" width="8" height="26"/><rect x="26" y="32" width="8" height="26"/><rect x="42" y="32" width="8" height="26"/><rect x="56" y="32" width="8" height="26"/><rect x="6" y="60" width="64" height="8"/></svg>
      <h3 class="heading">Financial Law</h3>
    </div>
    <div class="area">
      <svg viewBox="0 0 76 76" fill="#fff"><circle cx="38" cy="18" r="10"/><circle cx="16" cy="26" r="8"/><circle cx="60" cy="26" r="8"/><path d="M22 70c0-20 6-36 16-36s16 16 16 36z"/><path d="M2 60c0-16 6-26 14-26 4 0 7 2 9 6-3 6-5 13-5 20z"/><path d="M74 60c0-16-6-26-14-26-4 0-7 2-9 6 3 6 5 13 5 20z"/></svg>
      <h3 class="heading">Family Law</h3>
    </div>
    <div class="area">
      <svg viewBox="0 0 76 76" fill="#fff"><path d="M6 24h40v36H6zM46 34h12l12 14v12H46z"/><rect x="18" y="30" width="16" height="24" fill="#0c1e5b"/><rect x="23" y="32" width="6" height="20" fill="#fff"/><rect x="16" y="39" width="20" height="6" fill="#fff"/><circle cx="18" cy="62" r="7"/><circle cx="58" cy="62" r="7"/><circle cx="18" cy="62" r="3" fill="#0c1e5b"/><circle cx="58" cy="62" r="3" fill="#0c1e5b"/></svg>
      <h3 class="heading">Health Care Law</h3>
    </div>
    <div class="area">
      <svg viewBox="0 0 76 76" fill="#fff"><rect x="14" y="14" width="26" height="18" rx="2" transform="rotate(45 27 23)"/><rect x="34" y="30" width="10" height="40" rx="3" transform="rotate(-45 39 50)"/></svg>
      <h3 class="heading">Criminal Law</h3>
    </div>
  </div>
</section>

<section class="about" role="img" aria-label="Lawyers in a meeting with clients around a table">
  <h2 class="heading">About Us</h2>
  <p class="quote serif">All people are equal before the law. A good attorney is what makes a difference.</p>
  <p class="summary">At vero eos et accusamus et iusto odio dignissimos ducimus qui blanditiis praesentium voluptatum deleniti atque corrupti quos dolores et quas molestias excepturi sint occaecati cupiditate non provident, similique sunt in culpa qui officia deserunt mollitia animi...</p>
  <a class="btn-outline" href="#">Read More</a>
</section>

<section class="lawyers">
  <h2 class="section-title heading">Our Lawyers</h2>
  <p class="section-lead serif">We are a full service, general practice law firm, but we specialize in the areas of residential and commercial real estate transactions and litigation<br>and commercial transactions and litigation.</p>
  <div class="lawyer-grid">
    <article class="lawyer">
      <div class="photo" role="img" aria-label="Attorney in conversation with a client"></div>
      <h3 class="serif">Joris Vermaat</h3><div class="role">Attorney</div>
      <p>Lorem ipsum dolor sit met, conteturing elit. Phasellus pellentesque osure risus lacinia tristique Fusce sed massa</p>
      <a class="btn-solid" href="#">Read More</a>
    </article>
    <article class="lawyer">
      <div class="photo" role="img" aria-label="Attorney at her desk with a client"></div>
      <h3 class="serif">Karin Dorsman</h3><div class="role">Attorney</div>
      <p>Lorem ipsum dolor sit met, conteturing elit. Phasellus pellentesque osure risus lacinia tristique Fusce sed massa</p>
      <a class="btn-solid" href="#">Read More</a>
    </article>
    <article class="lawyer">
      <div class="photo" role="img" aria-label="Attorney in robe holding a gavel"></div>
      <h3 class="serif">Maarten Lindeboom</h3><div class="role">Attorney</div>
      <p>Lorem ipsum dolor sit met, conteturing elit. Phasellus pellentesque osure risus lacinia tristique Fusce sed massa</p>
      <a class="btn-solid" href="#">Read More</a>
    </article>
    <article class="lawyer">
      <div class="photo" role="img" aria-label="Attorney meeting clients at a table"></div>
      <h3 class="serif">Hilde Stoffels</h3><div class="role">Attorney</div>
      <p>Lorem ipsum dolor sit met, conteturing elit. Phasellus pellentesque osure risus lacinia tristique Fusce sed massa</p>
      <a class="btn-solid" href="#">Read More</a>
    </article>
  </div>
</section>

<section class="testimonials">
  <h2 class="heading">Testimonials</h2>
  <div class="avatar" role="img" aria-label="Portrait of the client giving the testimonial"></div>
  <blockquote>At vero eos et accusamus et iusto odio dignissimos ducimus qui blanditiis praesentium voluptatum deleniti atque corrupti quos dolores et quas molestias excepturi sint occaecati cupiditate non provident, similique sunt in culpa qui officia deserunt mollitia animi, id est laborum et dolorum fuga. Et harum quidem rerum facilis est et expedita distinctio.</blockquote>
  <cite>Sanne Veldkamp</cite>
  <div class="dots"><span></span><span class="on"></span><span></span></div>
</section>

<div class="map" role="img" aria-label="Map of the Netherlands showing office locations"></div>

<footer class="site-footer">
  <nav class="footer-nav">
    <a href="#">Home</a><a href="#">Practice Areas</a><a href="#">Lawyers</a><a href="#">News</a><a href="#">FAQ</a><a href="#">Contact</a>
  </nav>
  <p class="copyright">©2015 kwelderhofpunt.website. All rights reserved.</p>
  <div class="social"><span></span><span></span><span></span></div>
</footer>

</body>
</html>
```